Social Media Graphics - Harbor Climb REVISED

Create 6-7 individual social media graphics (square size) to encourage folks to join our online course called:

The Lantern Ledger Plan
How to Launch a Multi-Million Business From Scratch
Sign Up Today!

IMPORTANT: Make the largest and most prominent text on the graphic be: How to Launch a Multi-Million Business From Scratch

For the color scheme of the graphics, let's try a blue color palette; make sure the graphics appeal to both men and women

Make sure each graphic contains 1 of the 3 pics attached (crop pic as needed); and make sure one of the graphics is all TEXT only.

Target Market(s)

men and women looking to start a business

Industry/Entity Type

Entrepreneurship

Colors
0054AA
0677BA
7BADD7
CADEEF
E8F1F8

Requirements
Must have
• All the text and use the 3 pics provided; one graphic can be all text; Simple, modern design that's easy to read

```html
<!DOCTYPE html>
<html lang="en">
<head>
<meta charset="utf-8">
<title>The Lantern Ledger Plan – Sign Up Today</title>
<link href="https://fonts.googleapis.com/css2?family=Anton&family=Archivo+Black&family=Oswald:wght@500;600&display=swap" rel="stylesheet">
<style>
  :root {
    --blue-deep: #0054AA;
    --blue-mid: #0677BA;
    --blue-soft: #7BADD7;
    --blue-pale: #CADEEF;
    --blue-mist: #E8F1F8;
    --white: #FFFFFF;
  }
  html, body {
    margin: 0;
    padding: 0;
    width: 1200px;
    height: 1200px;
    overflow: hidden;
    background: var(--blue-mist);
  }
  .graphic {
    position: relative;
    width: 1200px;
    height: 1200px;
    overflow: hidden;
    background: var(--blue-mist);
  }
  .bands {
    position: absolute;
    inset: 0;
  }
  .ribbon {
    position: absolute;
    left: 102px;
    top: 0;
    width: 276px;
    height: 284px;
    filter: drop-shadow(-6px 6px 0 rgba(0, 40, 90, 0.25));
    z-index: 2;
  }
  .ribbon svg { display: block; }
  .ribbon-text {
    position: absolute;
    left: 0;
    top: 14px;
    width: 276px;
    text-align: center;
    font-family: "Anton", sans-serif;
    text-transform: uppercase;
    line-height: 1;
  }
  .ribbon-the {
    display: block;
    color: var(--white);
    font-size: 40px;
    text-align: left;
    padding-left: 18px;
  }
  .ribbon-name {
    display: block;
    color: var(--blue-deep);
    font-size: 62px;
    margin-top: 6px;
  }
  .masthead {
    position: absolute;
    left: 408px;
    top: 22px;
    margin: 0;
    font-family: "Anton", sans-serif;
    font-weight: 400;
    font-size: 118px;
    line-height: 1;
    letter-spacing: 4px;
    color: var(--white);
    text-transform: uppercase;
  }
  .hosts-photo {
    position: absolute;
    left: 564px;
    top: 296px;
    width: 636px;
    height: 720px;
    background: linear-gradient(100deg, #3a2520 0%, #d8435e 30%, #c93553 52%, #1c1c1e 72%, #0f0f10 100%);
    z-index: 1;
  }
  .headline {
    position: absolute;
    left: 32px;
    top: 322px;
    width: 520px;
    margin: 0;
    color: var(--blue-deep);
    text-transform: uppercase;
    font-weight: 400;
    z-index: 2;
  }
  .headline-lead {
    display: block;
    font-family: "Archivo Black", sans-serif;
    line-height: 1;
    white-space: nowrap;
    text-shadow: -3px 3px 0 rgba(0, 40, 90, 0.2);
  }
  .headline-lead.how { font-size: 108px; letter-spacing: 1px; }
  .headline-lead.launch { font-size: 100px; margin-top: -8px; letter-spacing: 0; }
  .headline-sub {
    display: block;
    font-family: "Oswald", sans-serif;
    font-weight: 600;
    font-size: 88px;
    line-height: 1;
    transform: scaleX(0.66);
    transform-origin: left center;
    white-space: nowrap;
    text-shadow: -3px 3px 0 rgba(0, 40, 90, 0.18);
  }
  .headline-sub.one { margin-top: 46px; padding-left: 14px; }
  .headline-sub.two { margin-top: 16px; }
  .headline-sub.three { margin-top: 20px; }
  .cta {
    position: absolute;
    left: 300px;
    top: 1070px;
    display: flex;
    align-items: center;
  }
  .cta-arrows { display: block; margin-right: 36px; }
  .cta-label {
    font-family: "Oswald", sans-serif;
    font-weight: 500;
    font-size: 104px;
    line-height: 1;
    color: var(--white);
    letter-spacing: 2px;
    transform: scaleX(0.82);
    transform-origin: left center;
    white-space: nowrap;
    text-transform: uppercase;
  }
</style>
</head>
<body>
<main class="graphic">
  <svg class="bands" width="1200" height="1200" viewBox="0 0 1200 1200" aria-hidden="true">
    <polygon points="0,0 1200,0 1200,148 0,182" fill="var(--blue-deep)"/>
    <polygon points="380,170 1200,148 1200,172 380,194" fill="var(--blue-soft)"/>
    <polygon points="0,1030 1200,1004 1200,1200 0,1200" fill="var(--blue-soft)"/>
    <polygon points="0,1050 1200,1026 1200,1200 0,1200" fill="var(--blue-deep)"/>
  </svg>

  <div class="ribbon">
    <svg width="276" height="284" viewBox="0 0 276 284" aria-hidden="true">
      <polygon points="0,0 276,0 276,284 138,226 0,284" fill="var(--blue-soft)"/>
    </svg>
    <div class="ribbon-text">
      <span class="ribbon-the">The</span>
      <span class="ribbon-name">Lantern</span>
      <span class="ribbon-name">Ledger</span>
    </div>
  </div>

  <h2 class="masthead">Plan</h2>

  <div class="hosts-photo" role="img" aria-label="Photo of the two course hosts, a smiling woman in a pink top with arms crossed and a smiling man in a dark jacket"></div>

  <h1 class="headline">
    <span class="headline-lead how">How to</span>
    <span class="headline-lead launch">Launch</span>
    <span class="headline-sub one">A Multi-Million</span>
    <span class="headline-sub two">Business</span>
    <span class="headline-sub three">From Scratch</span>
  </h1>

  <div class="cta">
    <svg class="cta-arrows" width="244" height="64" viewBox="0 0 244 64" aria-hidden="true">
      <polygon points="0,0 64,32 0,64" fill="var(--blue-soft)"/>
      <polygon points="90,0 154,32 90,64" fill="var(--blue-soft)"/>
      <polygon points="180,0 244,32 180,64" fill="var(--blue-soft)"/>
    </svg>
    <span class="cta-label">Sign Up Today!</span>
  </div>
</main>
</body>
</html>
```